Welding Fabrication and Inspection Business Card Design

Welding Fabrication and Inspection Services,

Business

Industrial Machinery ServicesMohammed Rahim30 Ballarat Street, Kelvin Ridge East.4187.QLD

```html
<!DOCTYPE html>
<html lang="en">
<head>
<meta charset="utf-8">
<title>Corvane Plant Services – Business Card</title>
<link rel="stylesheet" href="https://fonts.googleapis.com/css2?family=Open+Sans:wght@400;600&display=swap">
<style>
  :root {
    --backdrop: #1c2419;
    --card: #e3e9dc;
    --band: #7a1e24;
    --ink: #141414;
    --photo-red: #a6262c;
    --photo-dark: #2a2a2a;
    --ghost: #c9cfc0;
  }
  * { margin: 0; padding: 0; box-sizing: border-box; }
  html, body {
    width: 1200px; height: 952px; overflow: hidden;
    background: var(--backdrop);
    font-family: "Open Sans", sans-serif;
  }
  .card {
    position: absolute; left: 100px; top: 176px;
    width: 1000px; height: 600px;
    background: var(--card);
    border-radius: 28px;
    overflow: hidden;
  }
  .band { position: absolute; left: 0; width: 100%; height: 50px; background: var(--band); }
  .band--top { top: 60px; }
  .band--bottom { top: 470px; }
  .ghost-visual {
    position: absolute; left: 560px; top: 140px; width: 340px; height: 320px;
    background: radial-gradient(ellipse at center, var(--ghost), transparent 70%);
    opacity: .7;
  }
  .brand {
    position: absolute; left: 60px; top: 200px; width: 360px;
    font-weight: 600; font-size: 28px; color: var(--ink); line-height: 1.2;
    display: flex; align-items: center; gap: 14px;
  }
  .brand__dot { width: 22px; height: 22px; border-radius: 50%; background: var(--band); flex: none; }
  .product-visual {
    position: absolute; left: 160px; top: 320px; width: 200px; height: 120px;
    border-radius: 10px;
    background: linear-gradient(180deg, var(--photo-red) 0 45%, var(--photo-dark) 45% 100%);
  }
  .divider { position: absolute; left: 450px; top: 140px; width: 3px; height: 310px; background: var(--ink); }
  .name {
    position: absolute; left: 490px; top: 150px;
    font-size: 46px; font-weight: 400; color: var(--ink);
  }
  .address {
    position: absolute; left: 520px; top: 330px;
    font-size: 26px; line-height: 1.4; color: var(--ink); font-style: normal;
  }
</style>
</head>
<body>
  <div class="card">
    <div class="band band--top"></div>
    <div class="band band--bottom"></div>
    <div class="ghost-visual" role="img" aria-label="Faint background photo of welding equipment"></div>

    <div class="brand"><span class="brand__dot"></span><span>Corvane Plant Services</span></div>
    <div class="product-visual" role="img" aria-label="Photo of a red magnetic particle inspection yoke"></div>

    <div class="divider"></div>

    <h1 class="name">Tariq Osmani</h1>
    <address class="address">
      17 Windorah Street,<br>
      Kelvin Ridge East.<br>
      4187.QLD
    </address>
  </div>
</body>
</html>
```